Poster to advertise new mind coaching clinic

Create a single sided A4 colour poster using the text provided. Suggested image provided. You may want to suggest an alternative however images need to appeal to both male and female sports people.

Text:
One-to-one mind coaching
For recreational and competitive sports people
Learn the mental tools and techniques used by the top sports people to fulfil your potential

 Create well-formed and achievable goals
 Overcome limiting beliefs
 Accelerate mastery through modelling your heroes
 Learn how to use mental rehearsal to increase your chances of success
 Smash through belief ceilings
 Get into the zone to bring your ‘A-Game’ more often
Thursdays in central Twyford
5-8pm
For more information contact:
thebluekitecoaching@postmere.com
Tel: 07481 265314
www.the-blue-kite.co.uk

Target Market(s)

sports people

Industry/Entity Type

Clinic

Requirements
Must have
• All the content provided. Contact details.

```html
<!DOCTYPE html>
<html lang="en">
<head>
<meta charset="utf-8">
<title>The Blue Kite – One to One Mind Coaching</title>
<link rel="stylesheet" href="https://fonts.googleapis.com/css2?family=Exo+2:ital,wght@0,500;0,700;1,400;1,500;1,600;1,700&family=Roboto+Condensed:wght@700&display=swap">
<style>
  :root {
    --canvas-bg: #efeedd;
    --paper: #ffffff;
    --swoosh: #dcdcdd;
    --ink: #111111;
    --blue-dark: #1a5aa3;
    --blue-light: #4d94d9;
    --blue-text: #cfe3f7;
    --accent-red: #e8474c;
    --sun: #f7c21e;
    --sun-ring: #f5c01f;
    --twyford-red: #e85b52;
  }
  * { margin: 0; padding: 0; box-sizing: border-box; }
  html, body { width: 900px; height: 1200px; overflow: hidden; }
  body { background: var(--canvas-bg); font-family: "Exo 2", sans-serif; color: var(--ink); }

  .poster { position: absolute; left: 41px; top: 22px; width: 817px; height: 1158px; background: var(--paper); overflow: hidden; }
  .swoosh { position: absolute; left: 0; top: 0; }

  .thumb-photo { position: absolute; left: 24px; top: 28px; width: 122px; height: 132px;
    background: linear-gradient(90deg, #d9b49a 0%, #2f6fc0 30%, #e9d2c2 55%, #ef6f72 80%, #f4f4f4 100%); border-radius: 4px; opacity: .85; }

  .headline { position: absolute; right: 38px; top: 58px; font-size: 37px; font-style: italic; font-weight: 500; letter-spacing: .3px; white-space: nowrap; }
  .subhead { position: absolute; right: 38px; top: 101px; font-size: 22.5px; font-style: italic; font-weight: 400; white-space: nowrap; }

  .tab-arc { position: absolute; left: 148px; top: 122px; }
  .intro-panel { position: absolute; left: 0; top: 160px; width: 377px; height: 174px;
    background: linear-gradient(90deg, var(--blue-dark) 0%, var(--blue-light) 55%, var(--blue-dark) 100%);
    border-radius: 0 8px 8px 0; padding: 23px 0 0 44px; }
  .intro-panel p { font-size: 24px; line-height: 32px; font-style: italic; font-weight: 500; color: var(--blue-text); }
  .intro-panel strong { color: #ffffff; font-weight: 500; }

  .main-photo { position: absolute; left: 338px; top: 203px; width: 450px; height: 860px;
    background: radial-gradient(ellipse at 35% 35%, #3a7dcf 0%, #8fb3dd 30%, transparent 60%),
                radial-gradient(ellipse at 75% 30%, #f08080 0%, #f1c1b4 28%, transparent 55%),
                linear-gradient(180deg, #f1e3d8 0%, #3a3a3d 45%, #cfc5bd 70%, #ffffff 100%);
    opacity: .55; border-radius: 40px; }

  .benefits { position: absolute; left: 40px; top: 366px; list-style: none; }
  .benefits li { position: relative; padding-left: 47px; font-size: 17.5px; line-height: 23px; font-style: italic; font-weight: 600; margin-bottom: 23px; }
  .benefits li svg { position: absolute; left: 0; top: 3px; }

  .contact { position: absolute; left: 38px; top: 756px; }
  .contact-label { font-size: 17.5px; font-style: italic; font-weight: 600; }
  .contact-email { font-size: 21px; font-weight: 500; margin-top: 6px; }
  .contact-phone { font-family: "Roboto Condensed", sans-serif; font-size: 62px; font-weight: 700; line-height: 1; margin-top: 6px; letter-spacing: .5px; }

  .session-badge { position: absolute; left: 519px; top: 647px; width: 288px; height: 288px; border-radius: 50%; border: 4px solid var(--sun-ring); padding: 11px; }
  .session-badge .disc { width: 100%; height: 100%; border-radius: 50%; background: var(--sun); text-align: center; padding-top: 78px; }
  .session-day { font-family: "Roboto Condensed", sans-serif; font-size: 36px; font-weight: 700; line-height: 1; }
  .session-place { font-family: "Roboto Condensed", sans-serif; font-size: 27px; font-weight: 700; color: var(--twyford-red); margin-top: 6px; }
  .session-time { font-family: "Roboto Condensed", sans-serif; font-size: 17px; font-weight: 700; margin-top: 6px; }

  .brand { position: absolute; left: 36px; top: 1010px; display: flex; align-items: center; gap: 14px; }
  .brand-dot { width: 34px; height: 34px; border-radius: 50%; background: var(--blue-light); }
  .brand-name { font-size: 42px; font-weight: 700; color: var(--ink); }

  .web { position: absolute; right: 30px; top: 1102px; font-size: 18px; font-style: italic; }
</style>
</head>
<body>
<main class="poster">
  <svg class="swoosh" width="817" height="340" viewBox="0 0 817 340" aria-hidden="true">
    <path d="M340 0 H817 V330 C790 210 700 90 540 40 C470 18 400 6 340 0 Z" fill="var(--swoosh)"/>
  </svg>

  <div class="thumb-photo" role="img" aria-label="Small photo of a male and female athlete in sportswear"></div>

  <h1 class="headline">ONE TO ONE MIND COACHING</h1>
  <p class="subhead">For recreational and competitive sports people</p>

  <svg class="tab-arc" width="146" height="42" viewBox="0 0 146 42" aria-hidden="true">
    <path d="M6 42 A67 67 0 0 1 140 42" fill="none" stroke="var(--blue-light)" stroke-width="6"/>
  </svg>
  <section class="intro-panel">
    <p>Learn the <strong>Mental Tools</strong><br>&amp; the <strong>Techniques</strong> used by<br>the <strong>Top Sports People</strong><br>to <strong>Fulfil Your Potential</strong></p>
  </section>

  <div class="main-photo" role="img" aria-label="Photo of a male athlete in a blue vest and a female athlete in a pink sports top standing back to back"></div>

  <ul class="benefits">
    <li><svg width="30" height="30" viewBox="0 0 30 30"><path d="M4 15 H22 M15 7 L23 15 L15 23" fill="none" stroke="var(--accent-red)" stroke-width="4" stroke-linecap="round" stroke-linejoin="round"/></svg>Create well-formed and<br>achievable goals</li>
    <li><svg width="30" height="30" viewBox="0 0 30 30"><path d="M4 15 H22 M15 7 L23 15 L15 23" fill="none" stroke="var(--accent-red)" stroke-width="4" stroke-linecap="round" stroke-linejoin="round"/></svg>Overcome limiting beliefs</li>
    <li><svg width="30" height="30" viewBox="0 0 30 30"><path d="M4 15 H22 M15 7 L23 15 L15 23" fill="none" stroke="var(--accent-red)" stroke-width="4" stroke-linecap="round" stroke-linejoin="round"/></svg>Accelerate mastery<br>through modelling your heroes</li>
    <li><svg width="30" height="30" viewBox="0 0 30 30"><path d="M4 15 H22 M15 7 L23 15 L15 23" fill="none" stroke="var(--accent-red)" stroke-width="4" stroke-linecap="round" stroke-linejoin="round"/></svg>Learn how to use mental rehearsal<br>to increase your chances of success</li>
    <li><svg width="30" height="30" viewBox="0 0 30 30"><path d="M4 15 H22 M15 7 L23 15 L15 23" fill="none" stroke="var(--accent-red)" stroke-width="4" stroke-linecap="round" stroke-linejoin="round"/></svg>Smash through belief ceilings</li>
    <li><svg width="30" height="30" viewBox="0 0 30 30"><path d="M4 15 H22 M15 7 L23 15 L15 23" fill="none" stroke="var(--accent-red)" stroke-width="4" stroke-linecap="round" stroke-linejoin="round"/></svg>Get into the zone to bring your<br>‘A-Game’ more often</li>
  </ul>

  <section class="contact">
    <p class="contact-label">For more information contact:</p>
    <p class="contact-email">thebluekitecoaching@postmere.com</p>
    <p class="contact-phone">07481 265314</p>
  </section>

  <aside class="session-badge">
    <div class="disc">
      <p class="session-day">THURSDAYS</p>
      <p class="session-place">Central Twyford</p>
      <p class="session-time">5:00pm - 8:00pm</p>
    </div>
  </aside>

  <div class="brand">
    <span class="brand-dot"></span>
    <span class="brand-name">The Blue Kite</span>
  </div>

  <p class="web">www.the-blue-kite.co.uk</p>
</main>
</body>
</html>
```